Wholesale Fashion Agent

Industry/Entity Type

Fashion

Contact Information for Business Card

I have attached the previous logo, we are wanting to re-vamp with black and white only. Sharp and more modern.

Mirela Stonecroft Agencies back of card
address (to be advised, as we are moving)

MS Agencies front of card, with Fashion Agent on the front

```html
<!DOCTYPE html>
<html lang="en">
<head>
<meta charset="utf-8">
<title>Mirela Stonecroft Agencies – Business Cards</title>
<link rel="stylesheet" href="https://fonts.googleapis.com/css2?family=Oswald:wght@400;600&display=swap">
<style>
  :root {
    --stage: #2e2a28;
    --card-dark: #3b3b3d;
    --card-light: #dcdcdc;
    --circle-mid: #8d8d8d;
    --circle-deep: #767676;
    --dress-tone: #c6c6c6;
    --ink-white: #f2f2f2;
    --ink-grey: #b9b9b9;
    --ink-dark: #2b2b2b;
  }
  * { box-sizing: border-box; margin: 0; padding: 0; }
  html, body {
    width: 1200px; height: 762px; overflow: hidden;
    background: var(--stage);
    font-family: "Oswald", "Arial Narrow", sans-serif;
  }
  .stage { position: relative; width: 1200px; height: 762px; }

  .card {
    position: absolute; top: 216px;
    width: 540px; height: 330px;
    overflow: hidden;
    box-shadow: 0 10px 24px rgba(0,0,0,.45);
  }
  .card--contact { left: 40px; background: var(--card-dark); }
  .card--brand { left: 620px; background: var(--card-light); }

  /* contact side */
  .header-name {
    position: absolute; top: 26px; left: 28px;
    display: flex; align-items: center; gap: 10px;
    color: var(--ink-white); font-weight: 600; font-size: 19px;
    letter-spacing: .5px; text-transform: uppercase;
  }
  .header-name .mark {
    width: 20px; height: 20px; background: var(--ink-white);
  }
  .agency-circle {
    position: absolute; left: 36px; top: 82px;
    width: 190px; height: 190px; border-radius: 50%;
    background: var(--circle-mid);
    display: flex; align-items: center; justify-content: center;
    text-align: center;
    color: var(--ink-white); font-size: 25px; line-height: 1.1;
    text-transform: uppercase; letter-spacing: .5px;
  }
  .contact-list {
    position: absolute; left: 256px; top: 104px;
    list-style: none; color: var(--ink-grey);
    font-size: 13px; letter-spacing: .3px;
  }
  .contact-list li { display: flex; align-items: flex-start; gap: 9px; margin-bottom: 7px; }
  .contact-list .address { margin-bottom: 14px; padding-left: 21px; line-height: 1.35; }
  .contact-list svg { width: 12px; height: 12px; margin-top: 3px; flex: none; fill: var(--ink-grey); }

  /* brand side */
  .dress-art {
    position: absolute; left: 330px; top: 70px;
    width: 150px; height: 260px;
    background: linear-gradient(180deg, var(--dress-tone), #d2d2d2);
    border-radius: 60px 60px 10px 10px;
  }
  .brand-circle {
    position: absolute; left: 120px; top: 42px;
    width: 250px; height: 250px; border-radius: 50%;
    background: var(--circle-deep);
    display: flex; flex-direction: column; align-items: center; justify-content: center;
    color: var(--ink-dark); font-weight: 600; text-transform: uppercase;
    text-align: center; line-height: 1.05;
  }
  .brand-circle .brand-name { font-size: 40px; letter-spacing: 1px; }
  .brand-circle .brand-role { font-size: 22px; letter-spacing: 1px; margin-top: 6px; }
</style>
</head>
<body>
<main class="stage">

  <section class="card card--contact" aria-label="Contact side">
    <div class="header-name"><span class="mark"></span>Mirela Stonecroft Fashion Agent</div>
    <div class="agency-circle">Mirela<br>Stonecroft<br>Agencies</div>
    <ul class="contact-list">
      <li class="address">Unit 4/12 Harlow Lane Westbrook<br>Qld 4350 Australia</li>
      <li><svg viewBox="0 0 12 12"><path d="M2 1h3l1 3-2 1a7 7 0 0 0 3 3l1-2 3 1v3c-6 0-9-3-9-9z"/></svg>07 - 3900 2418</li>
      <li><svg viewBox="0 0 12 12"><rect x="1" y="3" width="10" height="7" rx="1"/><rect x="3" y="1" width="6" height="3"/></svg>07 - 3900 2419</li>
      <li><svg viewBox="0 0 12 12"><rect x="3" y="0.5" width="6" height="11" rx="1"/></svg>0400 555 731</li>
      <li><svg viewBox="0 0 12 12"><path d="M1 3h10v7H1z M1 3l5 4 5-4" fill="none" stroke="#b9b9b9" stroke-width="1.2"/></svg>mirela@msagencies.com.au</li>
      <li><svg viewBox="0 0 12 12"><circle cx="6" cy="6" r="5"/></svg>www.msagencies.com.au</li>
    </ul>
  </section>

  <section class="card card--brand" aria-label="Brand side">
    <div class="dress-art" role="img" aria-label="Illustration of a gown hanging on a hanger"></div>
    <div class="brand-circle">
      <span class="brand-name">MS Agencies</span>
      <span class="brand-role">Fashion Agent</span>
    </div>
  </section>

</main>
</body>
</html>
```